Brightwave Business Card

Professional Business Card Design required using the attached contact information.

Contact information can be rearranged as required.

The company is a new start up venture developing solar systems, the branding should be in keeping with that of one of the investors whose website is as follows https://www.quorvex.com/

```html
<!DOCTYPE html>
<html lang="en">
<head>
<meta charset="utf-8">
<title>Brightwave Renewables – Business Card</title>
<link href="https://fonts.googleapis.com/css2?family=Lato:wght@400;700&display=swap" rel="stylesheet">
<style>
  :root {
    --backdrop: #3b3430;
    --card: #2b313b;
    --card-edge: #1d2128;
    --ink-light: #f2f4f6;
    --ink-muted: #d9dde2;
    --accent: #2e6b50;
    --accent-bright: #3a8563;
  }
  * { margin: 0; padding: 0; box-sizing: border-box; }
  html, body {
    width: 1200px; height: 795px; overflow: hidden;
    background: var(--backdrop);
    font-family: "Lato", sans-serif;
  }
  .canvas {
    position: relative; width: 1200px; height: 795px;
    display: flex; align-items: center; justify-content: center; gap: 60px;
  }
  .card {
    position: relative; width: 510px; height: 291px;
    background: var(--card);
    border-radius: 3px;
    box-shadow: 0 12px 30px rgba(0,0,0,0.45);
    overflow: hidden;
  }
  .wordmark {
    color: var(--ink-light);
    font-weight: 400;
    text-transform: uppercase;
    letter-spacing: 0.12em;
    white-space: nowrap;
    display: flex; align-items: center; gap: 10px;
  }
  .wordmark-dot {
    width: 10px; height: 10px; border-radius: 50%;
    background: var(--accent-bright);
    flex: none;
  }
  .card-front .wordmark {
    position: absolute; left: 50%; top: 50%;
    transform: translate(-50%, -50%);
    font-size: 28px;
  }
  .card-back .wordmark {
    position: absolute; left: 34px; top: 34px;
    font-size: 24px;
  }
  .decor-circle {
    position: absolute; right: -70px; bottom: -90px;
    width: 290px; height: 290px; border-radius: 50%;
    background: var(--accent); opacity: 0.55;
  }
  .contact {
    position: absolute; left: 34px; top: 92px;
    color: var(--ink-muted); font-size: 14px; line-height: 1.35;
  }
  .contact-name {
    color: var(--accent-bright); font-weight: 700;
    text-transform: uppercase; font-size: 16px; letter-spacing: 0.02em;
  }
  .contact-role { margin-bottom: 12px; }
  .contact-address { margin-bottom: 12px; }
  .contact-line { display: flex; align-items: center; gap: 7px; }
  .contact-line svg { width: 10px; height: 10px; flex: none; fill: var(--accent-bright); }
</style>
</head>
<body>
<main class="canvas">
  <section class="card card-front">
    <div class="wordmark"><span>Brightwave</span><span class="wordmark-dot"></span><span>Renewables</span></div>
  </section>

  <section class="card card-back">
    <div class="wordmark"><span>Brightwave</span><span class="wordmark-dot"></span><span>Renewables</span></div>
    <div class="decor-circle"></div>
    <div class="contact">
      <p class="contact-name">Daniel Hollis</p>
      <p class="contact-role">Founder &amp; CEO</p>
      <p class="contact-address">318 Harbor Street<br>Portland, ME 04101</p>
      <p class="contact-line">
        <svg viewBox="0 0 10 10" aria-hidden="true"><path d="M2 0.5 L3.6 2.6 L2.8 3.6 Q4 6 6.4 7.2 L7.4 6.4 L9.5 8 L8.4 9.5 Q1.5 8.5 0.5 1.6 Z"/></svg>
        <span>+1 (555) 214-7730</span>
      </p>
      <p class="contact-line">
        <svg viewBox="0 0 10 10" aria-hidden="true"><path d="M0 2 H10 V8 H0 Z M0.8 2.6 L5 5.6 L9.2 2.6 V2.2 H0.8 Z" fill-rule="evenodd"/></svg>
        <span>daniel.hollis@brightwave-renewables.com</span>
      </p>
      <p class="contact-line">
        <svg viewBox="0 0 10 10" aria-hidden="true"><circle cx="5" cy="5" r="4.5"/></svg>
        <span>www.quorvex.com</span>
      </p>
    </div>
  </section>
</main>
</body>
</html>
```